Etiketten für Honiggläser gesucht
sehr kreativer Entwurf, in dem alle umfangreichen Vorgaben berücksichtigt wurden. q4712 ist sehr service- und lösungsorientiert. Arbeitet sehr schnell und exzellent.
Zielgruppe
Wir sind eine junge Hobbyimkerei und produzieren unsere eigenen Honigsorten. Zielgruppe ist jeder, der Honig mag.
Aufgabenstellung
Das zu entwerfende Etiketten_Design soll grundsätzlich ein „absoluter Hingucker“ werden, einen hohen Wiedererkennungswert besitzen, edel erscheinen und die Hochwertigkeit des Produktes zum Ausdruck bringen.
Im engeren Sinn sollen zwei voneinander unabhängige Etikettenteile entworfen werden, die aber im Design eine Einheit bilden sollen:
Beim ersten Teil handelt es sich um den sogenannten Gewährverschluss; er verbindet den Deckel mit dem Glas und zerreißt beim ersten Öffnen des Deckels. Der Gewährverschluss soll etwa 2 cm breit und 8 cm lang sein, und unter anderem von unserem Firmenlogo (siehe Datei) geziert werden. Bei dem Logo darf die Grafik und der Hintergrund in der Farbe variieren, und der Schriftzug kann entfallen, andere Änderungen dürfen jedoch nicht vorgenommen werden. Das Logo kann bei Bedarf gerne in anderen Dateiformaten zur Verfügung gestellt werden.
Den zweiten Teil stellt das eigentliche Produktetikett dar. Für dieses gibt es keine Größen- und Formvorgaben, allerdings müssen folgende Inhalte Berücksichtigung finden: Die Daten des Imkers (bitte folgende Platzhalter verwenden „Firmenname“, „Vorname1 & Vorname2 Nachname“, „Straße + Hausnummer“, „PLZ + Ortsname“, „Internetseite“ und „Emailadresse“) sowie den Angaben „500g“, „Mindestens haltbar bis:“ (dahinter oder darunter bitte weißen Freiraum für den Stempelaufdruck des Datums lassen), „Trocken, dunkel und vor Wärme geschützt lagern!“, und – ganz wichtig – die „Honigsorte“ mit den vorangestellten Worten „feinster deutscher“ (, z.B. „feinster deutscher Rapshonig“).
Jede Honigsorte soll mit einer Farbe verknüpft werden, sodass der Kunde schnell erkennen kann um welche Honigsorte es sich im Glas handelt (beispielsweise gelb für Rapshonig, grün für Waldhonig, usw.). Dafür soll die jeweilige Honigsortenfarbe, in welcher Form auch immer, das Etikett oder einen bestimmten Bereich davon domini..

```html
<!DOCTYPE html>
<html lang="de">
<head>
<meta charset="utf-8">
<title>Honigetiketten – Imkerei Kestner</title>
<link href="https://fonts.googleapis.com/css2?family=Barlow:wght@400;600&family=Barlow+Semi+Condensed:wght@400;500;600&display=swap" rel="stylesheet">
<style>
  :root{
    --ink:#2a2f33;
    --slate:#3c464c;
    --rose:#f8cacf;
    --raps-orange:#f6901e;
    --white:#ffffff;
    --rule:#9a9a9a;
  }
  html,body{margin:0;padding:0;width:1200px;height:1200px;overflow:hidden;background:var(--white);}
  body{position:relative;font-family:"Barlow Semi Condensed","Barlow",sans-serif;color:var(--ink);}

  .seal-strip{position:absolute;left:50px;top:257px;width:135px;height:536px;background:var(--slate);}
  .seal-brand{position:absolute;left:0;right:0;top:400px;text-align:center;color:var(--white);
    font-family:"Barlow Semi Condensed",sans-serif;font-weight:500;letter-spacing:.18em;font-size:12px;line-height:1.35;}
  .seal-brand .brand-dot{display:block;width:30px;height:30px;border-radius:50%;background:var(--white);margin:0 auto 10px;opacity:1;}

  .product-label{position:absolute;left:241px;top:257px;width:905px;height:310px;outline:1px solid var(--rule);}
  .product-label svg{display:block;}

  .variant-grid{position:absolute;left:241px;top:633px;display:grid;grid-template-columns:repeat(7,117px);
    column-gap:15.5px;row-gap:13px;}
  .variant{width:117px;height:95px;}
  .variant svg{display:block;width:117px;height:95px;}

  .hidden-defs{position:absolute;width:0;height:0;overflow:hidden;}
  .arc-word{font-family:"Barlow",sans-serif;font-weight:400;fill:var(--ink);}
  .arc-small{font-family:"Barlow",sans-serif;font-weight:400;fill:var(--ink);}
  .weight{font-family:"Barlow Semi Condensed",sans-serif;font-weight:600;fill:var(--ink);}
</style>
</head>
<body>

<svg class="hidden-defs" aria-hidden="true">
  <defs>
    <path id="card-arc-word" d="M38.5 56.6 A44 44 0 0 1 124.8 64.2"/>
    <path id="card-arc-top" d="M56 111.3 A50 50 0 0 1 32.7 55.1"/>
    <path id="card-arc-bottom" d="M63.7 105.2 A41 41 0 0 1 40.6 60.9"/>
    <path id="label-arc-word" d="M515.7 114.7 A112 112 0 0 1 731.3 133.5"/>
    <path id="label-arc-top" d="M565.6 257.2 A118 118 0 0 1 504.8 132.5"/>
    <path id="label-arc-bottom" d="M584.3 243.8 A98 98 0 0 1 524.5 136"/>
  </defs>
</svg>

<div class="seal-strip">
  <div class="seal-brand"><span class="brand-dot"></span>IMKEREI<br>KESTNER</div>
</div>

<div class="product-label">
  <svg width="905" height="310" viewBox="0 0 905 310">
    <rect width="905" height="310" fill="var(--rose)"/>
    <g font-family="Barlow Semi Condensed, sans-serif" fill="var(--ink)">
      <text x="23" y="40" font-size="16">Feinster deutscher Rapshonig</text>
      <text x="23" y="64" font-size="16" font-weight="600" letter-spacing="1">250g</text>
      <text x="23" y="91" font-size="14" letter-spacing="1.6">FIRMENNAME</text>
      <text x="23" y="121" font-size="15.5">Vorname1 &amp; Vorname2 Nachname,</text>
      <text x="23" y="143" font-size="15.5">Straße Hausnummer,</text>
      <text x="23" y="164" font-size="15.5">PLZ + Ortsname,</text>
      <text x="23" y="186" font-size="15.5">www.internetseite.de</text>
      <text x="23" y="208" font-size="15.5">Emailadresse</text>
    </g>
    <rect x="0" y="225" width="224" height="85" fill="var(--white)"/>
    <text x="23" y="250" font-family="Barlow Semi Condensed, sans-serif" font-size="15.5" fill="var(--ink)">Mindestens haltbar bis:</text>
    <circle cx="269" cy="245" r="14" fill="var(--ink)"/>
    <text x="269" y="276" text-anchor="middle" font-family="Barlow Semi Condensed, sans-serif" font-weight="500" font-size="9.5" letter-spacing="1.6" fill="var(--ink)">IMKEREI</text>
    <text x="269" y="289" text-anchor="middle" font-family="Barlow Semi Condensed, sans-serif" font-weight="500" font-size="9.5" letter-spacing="1.6" fill="var(--ink)">KESTNER</text>

    <polygon points="439,154 530,0 704,0 798,154 704,310 530,310" fill="var(--raps-orange)"/>
    <text class="arc-word" font-size="38"><textPath href="#label-arc-word" textLength="285" lengthAdjust="spacingAndGlyphs">RAPSHONIG</textPath></text>
    <text class="arc-small" font-size="15"><textPath href="#label-arc-top" textLength="112" lengthAdjust="spacing">Feinster</textPath></text>
    <text class="arc-small" font-size="15"><textPath href="#label-arc-bottom" textLength="108" lengthAdjust="spacing">deutscher</textPath></text>
    <circle cx="621" cy="162" r="60" fill="#e8841a" role="img" aria-label="Emblem: gekreuzte Honiglöffel, Blätter und Honigtropfen"/>
    <text x="690" y="250" class="weight" font-size="24" letter-spacing="2">250G</text>

    <text transform="translate(873 26) rotate(90)" font-family="Barlow Semi Condensed, sans-serif" font-size="13" fill="var(--ink)">Trocken, dunkel und vor Wärme geschützt lagern!</text>
  </svg>
</div>

<div class="variant-grid">
  <div class="variant"><svg viewBox="0 0 162 132"><rect width="162" height="132" fill="#19bde0"/><polygon points="4,66 40,0 122,0 158,66 122,132 40,132" fill="#ee4452"/><text class="arc-word" font-size="14"><textPath href="#card-arc-word" textLength="112" lengthAdjust="spacingAndGlyphs">AKAZIENHONIG</textPath></text><text class="arc-small" font-size="7"><textPath href="#card-arc-top">Feinster</textPath></text><text class="arc-small" font-size="7"><textPath href="#card-arc-bottom">deutscher</textPath></text><circle cx="81" cy="72" r="22" fill="#000" fill-opacity=".08" role="img" aria-label="Emblem mit Honiglöffeln"/><text x="104" y="112" class="weight" font-size="10">250G</text></svg></div>
  <div class="variant"><svg viewBox="0 0 162 132"><rect width="162" height="132" fill="#dcc9a4"/><polygon points="4,66 40,0 122,0 158,66 122,132 40,132" fill="#e4202a"/><text class="arc-word" font-size="14"><textPath href="#card-arc-word" textLength="112" lengthAdjust="spacingAndGlyphs">BLÜTENHONIG</textPath></text><text class="arc-small" font-size="7"><textPath href="#card-arc-top">Feinster</textPath></text><text class="arc-small" font-size="7"><textPath href="#card-arc-bottom">deutscher</textPath></text><circle cx="81" cy="72" r="22" fill="#000" fill-opacity=".08" role="img" aria-label="Emblem mit Honiglöffeln"/><text x="104" y="112" class="weight" font-size="10">250G</text></svg></div>
  <div class="variant"><svg viewBox="0 0 162 132"><rect width="162" height="132" fill="#f4911e"/><polygon points="4,66 40,0 122,0 158,66 122,132 40,132" fill="#a4c83c"/><text class="arc-word" font-size="11"><textPath href="#card-arc-word" textLength="116" lengthAdjust="spacingAndGlyphs">BUCHWEIZENHONIG</textPath></text><text class="arc-small" font-size="7"><textPath href="#card-arc-top">Feinster</textPath></text><text class="arc-small" font-size="7"><textPath href="#card-arc-bottom">deutscher</textPath></text><circle cx="81" cy="72" r="22" fill="#000" fill-opacity=".08" role="img" aria-label="Emblem mit Honiglöffeln"/><text x="104" y="112" class="weight" font-size="10">250G</text></svg></div>
  <div class="variant"><svg viewBox="0 0 162 132"><rect width="162" height="132" fill="#fff200"/><polygon points="4,66 40,0 122,0 158,66 122,132 40,132" fill="#f8c9cf"/><text class="arc-word" font-size="14"><textPath href="#card-arc-word" textLength="112" lengthAdjust="spacingAndGlyphs">EICHENHONIG</textPath></text><text class="arc-small" font-size="7"><textPath href="#card-arc-top">Feinster</textPath></text><text class="arc-small" font-size="7"><textPath href="#card-arc-bottom">deutscher</textPath></text><circle cx="81" cy="72" r="22" fill="#000" fill-opacity=".08" role="img" aria-label="Emblem mit Honiglöffeln"/><text x="104" y="112" class="weight" font-size="10">250G</text></svg></div>
  <div class="variant"><svg viewBox="0 0 162 132"><rect width="162" height="132" fill="#ec6aa0"/><polygon points="4,66 40,0 122,0 158,66 122,132 40,132" fill="#1f3b8f"/><text class="arc-word" font-size="9"><textPath href="#card-arc-word" textLength="116" lengthAdjust="spacingAndGlyphs">EDELKASTANIENHONIG</textPath></text><text class="arc-small" font-size="7"><textPath href="#card-arc-top">Feinster</textPath></text><text class="arc-small" font-size="7"><textPath href="#card-arc-bottom">deutscher</textPath></text><circle cx="81" cy="72" r="22" fill="#000" fill-opacity=".1" role="img" aria-label="Emblem mit Honiglöffeln"/><text x="104" y="112" class="weight" font-size="10">250G</text></svg></div>
  <div class="variant"><svg viewBox="0 0 162 132"><rect width="162" height="132" fill="#ee4452"/><polygon points="4,66 40,0 122,0 158,66 122,132 40,132" fill="#f8a71b"/><text class="arc-word" font-size="13"><textPath href="#card-arc-word" textLength="114" lengthAdjust="spacingAndGlyphs">FENCHELHONIG</textPath></text><text class="arc-small" font-size="7"><textPath href="#card-arc-top">Feinster</textPath></text><text class="arc-small" font-size="7"><textPath href="#card-arc-bottom">deutscher</textPath></text><circle cx="81" cy="72" r="22" fill="#000" fill-opacity=".08" role="img" aria-label="Emblem mit Honiglöffeln"/><text x="104" y="112" class="weight" font-size="10">250G</text></svg></div>
  <div class="variant"><svg viewBox="0 0 162 132"><rect width="162" height="132" fill="#d11349"/><polygon points="4,66 40,0 122,0 158,66 122,132 40,132" fill="#cde06f"/><text class="arc-word" font-size="15"><textPath href="#card-arc-word" textLength="108" lengthAdjust="spacingAndGlyphs">WALDHONIG</textPath></text><text class="arc-small" font-size="7"><textPath href="#card-arc-top">Feinster</textPath></text><text class="arc-small" font-size="7"><textPath href="#card-arc-bottom">deutscher</textPath></text><circle cx="81" cy="72" r="22" fill="#000" fill-opacity=".08" role="img" aria-label="Emblem mit Honiglöffeln"/><text x="104" y="112" class="weight" font-size="10">250G</text></svg></div>

  <div class="variant"><svg viewBox="0 0 162 132"><rect width="162" height="132" fill="#cfe070"/><polygon points="4,66 40,0 122,0 158,66 122,132 40,132" fill="#84aed3"/><text class="arc-word" font-size="11"><textPath href="#card-arc-word" textLength="116" lengthAdjust="spacingAndGlyphs">FRÜHTRACHTHONIG</textPath></text><text class="arc-small" font-size="7"><textPath href="#card-arc-top">Feinster</textPath></text><text class="arc-small" font-size="7"><textPath href="#card-arc-bottom">deutscher</textPath></text><circle cx="81" cy="72" r="22" fill="#000" fill-opacity=".08" role="img" aria-label="Emblem mit Honiglöffeln"/><text x="104" y="112" class="weight" font-size="10">250G</text></svg></div>
  <div class="variant"><svg viewBox="0 0 162 132"><rect width="162" height="132" fill="#b985b4"/><polygon points="4,66 40,0 122,0 158,66 122,132 40,132" fill="#66bb9a"/><text class="arc-word" font-size="15"><textPath href="#card-arc-word" textLength="108" lengthAdjust="spacingAndGlyphs">HEIDEHONIG</textPath></text><text class="arc-small" font-size="7"><textPath href="#card-arc-top">Feinster</textPath></text><text class="arc-small" font-size="7"><textPath href="#card-arc-bottom">deutscher</textPath></text><circle cx="81" cy="72" r="22" fill="#000" fill-opacity=".08" role="img" aria-label="Emblem mit Honiglöffeln"/><text x="104" y="112" class="weight" font-size="10">250G</text></svg></div>
  <div class="variant"><svg viewBox="0 0 162 132"><rect width="162" height="132" fill="#d11349"/><polygon points="4,66 40,0 122,0 158,66 122,132 40,132" fill="#d4458f"/><text class="arc-word" font-size="12"><textPath href="#card-arc-word" textLength="114" lengthAdjust="spacingAndGlyphs">HIMBEERHONIG</textPath></text><text class="arc-small" font-size="7"><textPath href="#card-arc-top">Feinster</textPath></text><text class="arc-small" font-size="7"><textPath href="#card-arc-bottom">deutscher</textPath></text><circle cx="81" cy="72" r="22" fill="#000" fill-opacity=".08" role="img" aria-label="Emblem mit Honiglöffeln"/><text x="104" y="112" class="weight" font-size="10">250G</text></svg></div>
  <div class="variant"><svg viewBox="0 0 162 132"><rect width="162" height="132" fill="#82d0df"/><polygon points="4,66 40,0 122,0 158,66 122,132 40,132" fill="#fff200"/><text class="arc-word" font-size="15"><textPath href="#card-arc-word" textLength="106" lengthAdjust="spacingAndGlyphs">KLEEHONIG</textPath></text><text class="arc-small" font-size="7"><textPath href="#card-arc-top">Feinster</textPath></text><text class="arc-small" font-size="7"><textPath href="#card-arc-bottom">deutscher</textPath></text><circle cx="81" cy="72" r="22" fill="#000" fill-opacity=".08" role="img" aria-label="Emblem mit Honiglöffeln"/><text x="104" y="112" class="weight" font-size="10">250G</text></svg></div>
  <div class="variant"><svg viewBox="0 0 162 132"><rect width="162" height="132" fill="#cfe5bb"/><polygon points="4,66 40,0 122,0 158,66 122,132 40,132" fill="#d2202a"/><text class="arc-word" font-size="10"><textPath href="#card-arc-word" textLength="116" lengthAdjust="spacingAndGlyphs">KORNBLUMENHONIG</textPath></text><text class="arc-small" font-size="7"><textPath href="#card-arc-top">Feinster</textPath></text><text class="arc-small" font-size="7"><textPath href="#card-arc-bottom">deutscher</textPath></text><circle cx="81" cy="72" r="22" fill="#000" fill-opacity=".08" role="img" aria-label="Emblem mit Honiglöffeln"/><text x="104" y="112" class="weight" font-size="10">250G</text></svg></div>
  <div class="variant"><svg viewBox="0 0 162 132"><rect width="162" height="132" fill="#64bc9a"/><polygon points="4,66 40,0 122,0 158,66 122,132 40,132" fill="#f47f26"/><text class="arc-word" font-size="14"><textPath href="#card-arc-word" textLength="112" lengthAdjust="spacingAndGlyphs">LINDENHONIG</textPath></text><text class="arc-small" font-size="7"><textPath href="#card-arc-top">Feinster</textPath></text><text class="arc-small" font-size="7"><textPath href="#card-arc-bottom">deutscher</textPath></text><circle cx="81" cy="72" r="22" fill="#000" fill-opacity=".08" role="img" aria-label="Emblem mit Honiglöffeln"/><text x="104" y="112" class="weight" font-size="10">250G</text></svg></div>
  <div class="variant"><svg viewBox="0 0 162 132"><rect width="162" height="132" fill="#fde8b6"/><polygon points="4,66 40,0 122,0 158,66 122,132 40,132" fill="#374650"/><text class="arc-word" font-size="10"><textPath href="#card-arc-word" textLength="116" lengthAdjust="spacingAndGlyphs">WEISSTANNENHONIG</textPath></text><text class="arc-small" font-size="7"><textPath href="#card-arc-top">Feinster</textPath></text><text class="arc-small" font-size="7"><textPath href="#card-arc-bottom">deutscher</textPath></text><circle cx="81" cy="72" r="22" fill="#000" fill-opacity=".12" role="img" aria-label="Emblem mit Honiglöffeln"/><text x="104" y="112" class="weight" font-size="10">250G</text></svg></div>

  <div class="variant"><svg viewBox="0 0 162 132"><rect width="162" height="132" fill="#fff28c"/><polygon points="4,66 40,0 122,0 158,66 122,132 40,132" fill="#f6901e"/><text class="arc-word" font-size="11"><textPath href="#card-arc-word" textLength="116" lengthAdjust="spacingAndGlyphs">LÖWENZAHNHONIG</textPath></text><text class="arc-small" font-size="7"><textPath href="#card-arc-top">Feinster</textPath></text><text class="arc-small" font-size="7"><textPath href="#card-arc-bottom">deutscher</textPath></text><circle cx="81" cy="72" r="22" fill="#000" fill-opacity=".08" role="img" aria-label="Emblem mit Honiglöffeln"/><text x="104" y="112" class="weight" font-size="10">250G</text></svg></div>
  <div class="variant"><svg viewBox="0 0 162 132"><rect width="162" height="132" fill="#06a99a"/><polygon points="4,66 40,0 122,0 158,66 122,132 40,132" fill="#e6137f"/><text class="arc-word" font-size="11"><textPath href="#card-arc-word" textLength="116" lengthAdjust="spacingAndGlyphs">OBSTBLÜTENHONIG</textPath></text><text class="arc-small" font-size="7"><textPath href="#card-arc-top">Feinster</textPath></text><text class="arc-small" font-size="7"><textPath href="#card-arc-bottom">deutscher</textPath></text><circle cx="81" cy="72" r="22" fill="#000" fill-opacity=".08" role="img" aria-label="Emblem mit Honiglöffeln"/><text x="104" y="112" class="weight" font-size="10">250G</text></svg></div>
  <div class="variant"><svg viewBox="0 0 162 132"><rect width="162" height="132" fill="#f6c9cf"/><polygon points="4,66 40,0 122,0 158,66 122,132 40,132" fill="#dac9a4"/><text class="arc-word" font-size="12"><textPath href="#card-arc-word" textLength="114" lengthAdjust="spacingAndGlyphs">PHAZELIAHONIG</textPath></text><text class="arc-small" font-size="7"><textPath href="#card-arc-top">Feinster</textPath></text><text class="arc-small" font-size="7"><textPath href="#card-arc-bottom">deutscher</textPath></text><circle cx="81" cy="72" r="22" fill="#000" fill-opacity=".08" role="img" aria-label="Emblem mit Honiglöffeln"/><text x="104" y="112" class="weight" font-size="10">250G</text></svg></div>
  <div class="variant"><svg viewBox="0 0 162 132"><rect width="162" height="132" fill="#0a8c6e"/><polygon points="4,66 40,0 122,0 158,66 122,132 40,132" fill="#fff200"/><text class="arc-word" font-size="15"><textPath href="#card-arc-word" textLength="108" lengthAdjust="spacingAndGlyphs">RAPSHONIG</textPath></text><text class="arc-small" font-size="7"><textPath href="#card-arc-top">Feinster</textPath></text><text class="arc-small" font-size="7"><textPath href="#card-arc-bottom">deutscher</textPath></text><circle cx="81" cy="72" r="22" fill="#000" fill-opacity=".08" role="img" aria-label="Emblem mit Honiglöffeln"/><text x="104" y="112" class="weight" font-size="10">250G</text></svg></div>
  <div class="variant"><svg viewBox="0 0 162 132"><rect width="162" height="132" fill="#d7202a"/><polygon points="4,66 40,0 122,0 158,66 122,132 40,132" fill="#ffffff"/><text class="arc-word" font-size="9"><textPath href="#card-arc-word" textLength="116" lengthAdjust="spacingAndGlyphs">SOMMERTRACHTHONIG</textPath></text><text class="arc-small" font-size="7"><textPath href="#card-arc-top">Feinster</textPath></text><text class="arc-small" font-size="7"><textPath href="#card-arc-bottom">deutscher</textPath></text><circle cx="81" cy="72" r="22" fill="#000" fill-opacity=".06" role="img" aria-label="Emblem mit Honiglöffeln"/><text x="104" y="112" class="weight" font-size="10">250G</text></svg></div>
  <div class="variant"><svg viewBox="0 0 162 132"><rect width="162" height="132" fill="#cfe070"/><polygon points="4,66 40,0 122,0 158,66 122,132 40,132" fill="#3aaa48"/><text class="arc-word" font-size="9"><textPath href="#card-arc-word" textLength="116" lengthAdjust="spacingAndGlyphs">SONNENBLUMENHONIG</textPath></text><text class="arc-small" font-size="7"><textPath href="#card-arc-top">Feinster</textPath></text><text class="arc-small" font-size="7"><textPath href="#card-arc-bottom">deutscher</textPath></text><circle cx="81" cy="72" r="22" fill="#000" fill-opacity=".08" role="img" aria-label="Emblem mit Honiglöffeln"/><text x="104" y="112" class="weight" font-size="10">250G</text></svg></div>
</div>

</body>
</html>
```